Kestmar Conflict Varnok Legion Memoir Book Cover Design

We need a book cover design for a Russian kestmar conflict memoir.
Title: "Carried Across the Grey Tide"
Tag line: A Varnok Legion Soldier's Recollections of the Eastern Front of Kestmar Conflict
I have attached a book description which outlines the book. This is to go on the back cover.
I have attached images of book covers of the style we are looking for. Being Russia and War.
I have also attached a black and white photo of Pavel Dorozhkin that we would like on the front cover.
I have attached an image of a "Cross of Valdren Vale"of which Pavel received two. If an image of this could be incorporated on the front or back.
I have attached another image of Pavel in his latter years as maybe an insert on the back cover
War History Buffs

```html
<!DOCTYPE html>
<html lang="en">
<head>
<meta charset="utf-8">
<title>Carried Across the Grey Tide — Book Cover</title>
<link rel="stylesheet" href="https://fonts.googleapis.com/css2?family=Bebas+Neue&family=Archivo+Black&family=Montserrat:wght@700&display=swap">
<style>
  :root {
    --canvas: #ffffff;
    --paper: #e9e2d3;
    --paper-warm: #ddd6c6;
    --fur-grey: #c9c8c4;
    --face-grey: #b9b6af;
    --tunic-grey: #6f6f6e;
    --tunic-dark: #4f4f4f;
    --ink: #121212;
    --blood-red: #7f1514;
    --medal-red: #c0241d;
    --medal-dark: #7d0f0c;
    --medal-light: #e9e2d3;
  }
  * { margin: 0; padding: 0; box-sizing: border-box; }
  html, body {
    width: 1200px;
    height: 1200px;
    overflow: hidden;
    background: var(--canvas);
  }
  .book-cover {
    position: absolute;
    left: 274px;
    top: 42px;
    width: 680px;
    height: 1139px;
    overflow: hidden;
    background: var(--paper);
  }
  .portrait-photo {
    position: absolute;
    inset: 0;
    background:
      radial-gradient(ellipse 30% 13% at 49% 32%, rgba(205,204,200,0.95), rgba(205,204,200,0) 100%),
      radial-gradient(ellipse 24% 22% at 50% 55%, rgba(178,175,168,0.9), rgba(178,175,168,0) 100%),
      radial-gradient(ellipse 70% 30% at 50% 100%, rgba(79,79,79,0.9), rgba(79,79,79,0) 100%),
      linear-gradient(180deg,
        var(--paper) 0%,
        var(--paper-warm) 35%,
        #d2cdc2 55%,
        #a6a4a0 64%,
        var(--tunic-grey) 72%,
        #6a6a69 88%,
        var(--tunic-dark) 100%);
  }
  .cover-type {
    position: absolute;
    inset: 0;
    width: 680px;
    height: 1139px;
  }
  .author-name {
    font-family: "Bebas Neue", "Oswald", sans-serif;
    fill: var(--blood-red);
  }
  .title-upper {
    font-family: "Archivo Black", "Arial Black", sans-serif;
    fill: var(--ink);
  }
  .title-lower {
    font-family: "Bebas Neue", "Oswald", sans-serif;
  }
  .title-lower .ink { fill: var(--ink); }
  .title-lower .red { fill: var(--blood-red); }
  .title-lower .on-medal { fill: var(--medal-light); }
  .tagline {
    font-family: "Montserrat", "Helvetica", sans-serif;
    font-weight: 700;
    fill: var(--ink);
  }
</style>
</head>
<body>
  <main class="book-cover">
    <div class="portrait-photo" role="img" aria-label="Black and white portrait photograph of Pavel Dorozhkin in a fur winter hat and uniform tunic with medals, on aged paper"></div>

    <svg class="cover-type" viewBox="0 0 680 1139" xmlns="http://www.w3.org/2000/svg">
      <defs>
        <radialGradient id="medalTone" cx="0.4" cy="0.35" r="0.7">
          <stop offset="0" stop-color="var(--medal-red)"/>
          <stop offset="1" stop-color="var(--medal-dark)"/>
        </radialGradient>
      </defs>

      <text class="author-name" x="212" y="127" font-size="133" textLength="265" lengthAdjust="spacing">PAVEL</text>
      <text class="author-name" x="68" y="236" font-size="133" textLength="556" lengthAdjust="spacing">DOROZHKIN</text>

      <text class="title-upper" x="43" y="813" font-size="70" textLength="577" lengthAdjust="spacingAndGlyphs">CARRIED ACROSS THE</text>

      <g class="title-lower" font-size="198">
        <text class="ink" x="44" y="965" textLength="301" lengthAdjust="spacingAndGlyphs">GREY</text>
        <text class="red" x="381" y="965" textLength="66" lengthAdjust="spacingAndGlyphs">T</text>
        <circle cx="474" cy="893" r="62" fill="url(#medalTone)" role="img" aria-label="Cross of Valdren Vale medal"/>
        <text class="on-medal" x="459" y="965" textLength="30" lengthAdjust="spacingAndGlyphs">I</text>
        <text class="red" x="502" y="965" textLength="122" lengthAdjust="spacingAndGlyphs">DE</text>
      </g>

      <text class="tagline" x="43" y="1002" font-size="26" textLength="581" lengthAdjust="spacingAndGlyphs">A VARNOK LEGION SOLDIER'S RECOLLECTIONS OF THE</text>
      <text class="tagline" x="340" y="1028" font-size="26" text-anchor="middle" textLength="440" lengthAdjust="spacingAndGlyphs">EASTERN FRONT OF KESTMAR CONFLICT</text>
    </svg>
  </main>
</body>
</html>
```